Real Estate Website - Phase I

We are looking to re-design our company website completely.
This will be for a real estate company which focuses on multiple lines of business/customers, including

1) Buyers - Investors, Owner Occupants
2) Sellers - Short Sales, Limited Services/Flat Fee, and Corporate/REO clients (the last being our core current customer)
3) Other Services: Default Services, Institutional Property Management, Field and Inspection Services
4) Agent FAQ's, instructions, etc to tie into our web-based offer management systems

For a brief understanding of what we do - Please see www.tvlomar.com. Current site does not address all of our current services.

Website must be able to be edited/added onto over time. We are also looking at redirects so that certain pages/sections can be given unique domain names to drive core customers to.

We work both with normal agents and buyers and large scale financial institutions, therefore our focus must be specific to each unique group based on the applicable page(s).

We had an incorrect amount in this brief.  It has since been corrected.

Please re-review.

Industry/Entity Type

Real Estate

Requirements
Must have
• *Property Search/Display - By various criteria AND by map
*Property Management back end for putting in new properties
*MObile Version or Mobile Friendly
*Analytics
*Contact Management and Lead Capture functions, including ability to export or use from site for email marketing campaigns. Lead capture must be able to sort by various criteria to tailor campaigns, ability to send out auto notices to staff and those signing up, etc.
* Signup option w/ functions for viewing not yet on market properties (subscription). This needs to be able to let buyers set search criteria and be auto notified whenever a property was listed or adjusted that met their criteria.
* SEO Optimization
* Syndication options to allow ease of syndication
* FAQ's and assistance pages to agents working with us
* Blog, social media boxes
* Ability for buyers to submit initial offers direct
* Functions and pages specific to below, with ability to cross promote and track (inquiry forms, etc to the below)
*Dedicated or preferred lender(s)
* Preferred vendors, etc

```html
<!DOCTYPE html>
<html lang="en">
<head>
<meta charset="utf-8">
<title>Harbor Line REO</title>
<link href="https://fonts.googleapis.com/css2?family=Arimo:wght@400;700&family=Libre+Baskerville:wght@700&display=swap" rel="stylesheet">
<style>
:root{
  --navy:#1d2a78;
  --navy-dark:#0f1747;
  --blue:#0a4fa6;
  --blue-light:#1e6fcc;
  --gold:#f2b705;
  --gold-dark:#c98a00;
  --beige:#fdf1d8;
  --page:#eceae6;
  --panel:#ffffff;
  --line:#d6d6d6;
  --text:#333333;
  --muted:#666666;
  --price:#d8101a;
  --link:#1a2bb0;
}
*{box-sizing:border-box;margin:0;padding:0}
html,body{width:1200px;height:2297px;overflow:hidden}
body{font-family:"Arimo",Arial,sans-serif;color:var(--text);background:var(--page)}
.page{position:relative;width:1200px;height:2297px;overflow:hidden;background:#f1f0ee}
.abs{position:absolute}
.header{left:0;top:0;width:1200px;height:182px;background:linear-gradient(#f2f2f2,#e6e6e6)}
.brand{left:76px;top:34px;display:flex;align-items:center;gap:14px}
.brand-mark{width:80px;height:92px;background:var(--navy)}
.brand-name{font-family:"Libre Baskerville",Georgia,serif;font-weight:700;font-size:34px;color:var(--navy);line-height:1.15;width:240px}
.login-tab{left:889px;top:10px;width:248px;height:38px;background:var(--navy);clip-path:polygon(0 0,100% 0,94% 100%,6% 100%);color:#fff;font-size:14px;display:flex;align-items:center;justify-content:center;gap:8px}
.contact-line{left:946px;font-size:19px;font-weight:700;color:var(--navy);display:flex;align-items:center;gap:14px}
.nav{left:61px;top:183px;width:1078px;height:54px;background:linear-gradient(#1a6ed0,#0a3f8f);border-radius:4px;display:flex;align-items:center;justify-content:space-around;padding:0 14px}
.nav a{color:#fff;font-size:15px;text-decoration:none}
.hero{left:61px;top:248px;width:1078px;height:459px;background:#fff;border:1px solid var(--line);padding:7px}
.hero-photo{width:100%;height:100%;background:linear-gradient(#3f7fd6 0%,#8fb8e8 35%,#a5553a 55%,#7a3a26 80%,#556040 100%)}
.hero-arrow{top:277px;width:38px;height:38px;border-radius:50%;background:#fff}
.hero-caption{left:68px;top:608px;width:1064px;height:89px;background:rgba(0,0,0,.62)}
.hero-title{left:87px;top:620px;color:#fff;font-size:27px;letter-spacing:.5px}
.hero-sub{left:87px;top:656px;color:#fff;font-size:18px}
.btn-gold{background:linear-gradient(#f4c12a,#c98300);color:#1e1a10;font-weight:700;border:1px solid #8a5a00;display:flex;align-items:center;justify-content:center;gap:8px}
.know-more{left:595px;top:640px;width:180px;height:43px;font-size:18px}
.box{background:var(--panel);border:1px solid var(--line)}
.search-panel{left:61px;top:783px;width:738px;height:532px;padding:12px}
.search-inner{width:100%;height:100%;background:var(--beige)}
.h-section{font-size:24px;font-weight:700;color:#2b2b2b}
.rule{height:3px;background:#c8b79c}
.lbl{font-size:15px;color:#333;text-align:right;width:170px}
.field{height:32px;background:#fff;border:1px solid #a9a9a9;font-size:13px;color:#999;padding:7px 8px;white-space:nowrap;overflow:hidden}
.select{padding-right:28px}
.select::after{content:"";position:absolute;right:4px;top:6px;width:18px;height:18px;border:1px solid #888;background:#eee}
.radio{display:inline-flex;align-items:center;gap:6px;margin-right:20px;font-size:15px}
.radio i{width:13px;height:13px;border-radius:50%;border:1px solid #888;background:#fff;display:inline-block}
.radio i.on{background:radial-gradient(#333 35%,#fff 40%)}
.map-box{left:818px;top:783px;width:321px;height:627px;padding:15px 10px}
.blue-head{background:var(--blue);color:#fff;font-weight:700;text-align:center;display:flex;align-items:center;justify-content:center}
.map-area{margin-top:10px;width:299px;height:464px;background:linear-gradient(135deg,#eee3c9,#f3e9a8 40%,#e8e0cf 70%,#cfe3b6)}
.map-tabs{display:flex;width:299px;border:1px solid #777;height:23px;font-size:13px}
.map-tabs span{flex:1;text-align:center;line-height:21px;border-right:1px solid #777}
.map-tabs span:last-child{border-right:0}
.latest-head{left:67px;top:1343px;width:726px;height:43px;background:var(--gold);display:flex;align-items:center;justify-content:space-between;padding:0 14px}
.latest-head h2{font-size:27px;color:#1c2566}
.latest-head a{font-size:13px;color:#fff;font-weight:700;text-decoration:underline}
.card{top:1410px;width:235px;height:344px;padding:10px}
.card-photo{width:100%;height:185px;background:linear-gradient(#3d7a3a,#c3642d 45%,#d08a45 70%,#5a9e2f)}
.card-title{margin-top:25px;font-size:16px;line-height:1.25;color:#222}
.card-sub{font-size:13px;color:var(--link);margin-top:4px}
.card-foot{position:absolute;left:10px;right:10px;top:289px;border-top:1px solid var(--line);padding-top:14px;display:flex;justify-content:space-between;font-size:14px}
.card-foot .price{color:var(--price)}
.card-foot a{color:var(--price);text-decoration:underline}
.email-box{left:818px;top:1452px;width:321px;height:226px;padding:12px 9px}
.fb-box{left:818px;top:1689px;width:321px;height:352px;padding:12px 10px}
.fb-inner{border:1px solid #bbb;height:100%;position:relative}
.fb-head{height:30px;background:#eef0f5;border-bottom:1px solid #ccc;font-size:14px;font-weight:700;color:#333;padding:7px 10px}
.fan{position:absolute;width:57px;text-align:center;font-size:11px;color:#666}
.fan i{display:block;width:57px;height:57px;background:linear-gradient(#b89072,#6b5245);margin-bottom:4px}
.promo{top:1796px;height:164px;padding:10px}
.promo-fill{width:100%;height:100%;position:relative}
.footer-nav{left:0;top:2069px;width:1200px;height:37px;background:var(--gold);display:flex;align-items:center;justify-content:center;gap:14px;font-size:14px;color:#222}
.footer{left:0;top:2106px;width:1200px;height:191px;background:linear-gradient(var(--navy-dark),#2b3a9a 60%,#3747ad)}
.office{color:#fff;font-size:14px;line-height:20.5px;top:2128px}
.office b{display:block}
.social{top:2156px;width:34px;height:34px;border-radius:50%}
</style>
</head>
<body>
<div class="page">

  <header class="abs header"></header>
  <div class="abs brand">
    <div class="brand-mark"></div>
    <div class="brand-name">HARBOR LINE REO</div>
  </div>
  <div class="abs login-tab"><span>Agent Login</span><span>|</span><span>Client Login</span></div>
  <div class="abs contact-line" style="top:88px">
    <svg width="26" height="26" viewBox="0 0 26 26"><circle cx="13" cy="13" r="13" fill="#2d8fd8"/><path d="M9 7c1 0 2 3 2 4s-1 1-1 2 2 3 3 3 1-1 2-1 4 1 4 2-1 3-3 3C11 20 6 15 6 10c0-2 2-3 3-3z" fill="#fff"/></svg>
    <span>555-221-0032</span>
  </div>
  <div class="abs contact-line" style="top:130px">
    <svg width="26" height="20" viewBox="0 0 26 20"><rect width="26" height="20" rx="2" fill="#f2b705"/><path d="M1 2l12 9 12-9" stroke="#fff" stroke-width="2" fill="none"/></svg>
    <span>info@tvlomar.com</span>
  </div>

  <nav class="abs nav">
    <a>Home</a><a>Buyers</a><a>Sellers</a><a>Agents</a><a>Property Management</a><a>Field &amp; Inspection Services</a><a>Latest News</a><a>Blog</a><a>Contact</a>
  </nav>

  <section class="abs hero">
    <div class="hero-photo" role="img" aria-label="Photo of a red brick two-storey house under a blue sky"></div>
  </section>
  <div class="abs hero-arrow" style="left:1019px"><svg width="38" height="38"><path d="M22 12l-7 7 7 7" stroke="#222" stroke-width="3" fill="none"/></svg></div>
  <div class="abs hero-arrow" style="left:1065px"><svg width="38" height="38"><path d="M16 12l7 7-7 7" stroke="#222" stroke-width="3" fill="none"/></svg></div>
  <div class="abs hero-caption"></div>
  <div class="abs hero-title">GREEN HOUSE, OKALAHAM,</div>
  <div class="abs hero-sub">Lorel Ipsum Dolor Sit amet, For more information click here</div>
  <div class="abs btn-gold know-more">KNOW MORE <span>&#187;&#187;&#187;</span></div>

  <section class="abs box search-panel"><div class="search-inner"></div></section>
  <h2 class="abs h-section" style="left:88px;top:810px">SEARCH PROPERTY</h2>
  <div class="abs rule" style="left:84px;top:851px;width:690px"></div>
  <div class="abs" style="left:84px;top:873px;font-size:15px">Properties For :
    <span style="margin-left:12px"></span><span class="radio"><i class="on"></i>All</span><span class="radio"><i></i>Buy</span><span class="radio"><i></i>Rent</span></div>
  <div class="abs lbl" style="left:21px;top:920px">Locations :</div>
  <div class="abs field" style="left:200px;top:913px;width:209px">All Locations</div>
  <div class="abs lbl" style="left:362px;top:920px">Area (Sq M.) :</div>
  <div class="abs field select" style="left:541px;top:913px;width:204px">All Area</div>
  <div class="abs lbl" style="left:21px;top:966px">Price Range :</div>
  <div class="abs field select" style="left:200px;top:959px;width:209px">All Price Range in $</div>
  <div class="abs lbl" style="left:362px;top:966px">Keyword :</div>
  <div class="abs field" style="left:541px;top:959px;width:204px">City, Stateor Zip Code</div>
  <div class="abs lbl" style="left:21px;top:1011px">Bedrooms :</div>
  <div class="abs field select" style="left:200px;top:1004px;width:77px">All</div>
  <div class="abs lbl" style="left:21px;top:1053px">Bathrooms :</div>
  <div class="abs field select" style="left:200px;top:1046px;width:77px">All</div>
  <div class="abs btn-gold" style="left:199px;top:1101px;width:271px;height:46px;font-size:17px">SEARCH PROPERTIES
    <svg width="30" height="30" viewBox="0 0 30 30"><circle cx="17" cy="12" r="8" stroke="#222" stroke-width="3" fill="none"/><path d="M11 18l-8 8" stroke="#222" stroke-width="4"/></svg></div>
  <div class="abs rule" style="left:84px;top:1159px;width:690px"></div>
  <h2 class="abs h-section" style="left:88px;top:1196px">SEARCH BY PROPERTY ID</h2>
  <div class="abs lbl" style="left:21px;top:1250px;width:166px">Property ID :</div>
  <div class="abs field" style="left:200px;top:1243px;width:232px"></div>
  <div class="abs btn-gold" style="left:441px;top:1243px;width:129px;height:34px;font-size:16px">SEARCH
    <svg width="20" height="20" viewBox="0 0 30 30"><circle cx="17" cy="12" r="8" stroke="#222" stroke-width="3" fill="none"/><path d="M11 18l-8 8" stroke="#222" stroke-width="4"/></svg></div>

  <aside class="abs box map-box">
    <div class="blue-head" style="height:50px;font-size:26px">SEARCH BY MAP</div>
    <div class="map-area" role="img" aria-label="Street map of a metro area with property markers"></div>
    <div class="map-tabs"><span style="color:#c00">Search</span><span>List</span><span>Location</span><span>Disclaimer</span></div>
    <div style="font-size:12px;margin-top:12px;color:#333">Showing 1-50 of 300 properties</div>
    <div style="font-size:12px;color:var(--link)">Previous set &nbsp; <u>Next set</u></div>
  </aside>

  <div class="abs latest-head"><h2>LATEST PROPERTIES</h2><a>See More</a></div>

  <article class="abs box card" style="left:61px">
    <div class="card-photo" role="img" aria-label="Photo of a large timber house on a green lawn"></div>
    <div class="card-title">Stunning Home Built in The Estate of The Ridge</div>
    <div class="card-sub">Lorem ipsum dolotr sit</div>
    <div class="card-foot"><span class="price">$36589.00</span><a>More Info</a></div>
  </article>
  <article class="abs box card" style="left:311px">
    <div class="card-photo" role="img" aria-label="Photo of a large timber house on a green lawn"></div>
    <div class="card-title">Stunning Home Built in The Estate of The Ridge</div>
    <div class="card-sub">Lorem ipsum dolotr sit</div>
    <div class="card-foot"><span class="price">$36589.00</span><a>More Info</a></div>
  </article>
  <article class="abs box card" style="left:564px">
    <div class="card-photo" role="img" aria-label="Photo of a large timber house on a green lawn"></div>
    <div class="card-title">Stunning Home Built in The Estate of The Ridge</div>
    <div class="card-sub">Lorem ipsum dolotr sit</div>
    <div class="card-foot"><span class="price">$36589.00</span><a>More Info</a></div>
  </article>

  <aside class="abs box email-box">
    <div class="blue-head" style="height:49px;font-size:23px">JOIN EMAIL LIST</div>
    <div style="font-size:13px;margin-top:18px;color:#444">To stay informed about our services</div>
    <div class="field" style="margin-top:16px;width:300px;height:42px;padding-top:13px;font-size:12px">Type Your Email id</div>
    <div class="btn-gold" style="margin-top:14px;width:132px;height:45px;font-size:18px">SUBSCRIBE</div>
  </aside>

  <aside class="abs box fb-box">
    <div class="fb-inner">
      <div class="fb-head">Find us on Social</div>
      <div style="position:absolute;left:14px;top:40px;width:40px;height:44px;background:linear-gradient(#c9b6a4,#7d6a5c)" role="img" aria-label="Page profile picture"></div>
      <div style="position:absolute;left:66px;top:40px;font-size:15px;font-weight:700;color:var(--link)">HARBOR LINE REO</div>
      <div style="position:absolute;left:66px;top:66px;font-size:12px">You like this. <span style="color:var(--link)">Unlike</span></div>
      <div style="position:absolute;left:10px;top:104px;font-size:12px">338 people like <b>Harbor Line REO</b></div>
      <div class="fan" style="left:10px;top:130px"><i role="img" aria-label="Fan photo"></i>Marla</div>
      <div class="fan" style="left:82px;top:130px"><i role="img" aria-label="Fan photo"></i>Bettina</div>
      <div class="fan" style="left:154px;top:130px"><i role="img" aria-label="Fan photo"></i>Oscar</div>
      <div class="fan" style="left:224px;top:130px"><i role="img" aria-label="Fan photo"></i>Nora</div>
      <div class="fan" style="left:10px;top:209px"><i role="img" aria-label="Fan photo"></i>Rosa</div>
      <div class="fan" style="left:82px;top:209px"><i role="img" aria-label="Fan photo"></i>Paula</div>
      <div class="fan" style="left:154px;top:209px"><i role="img" aria-label="Fan photo"></i>Vince</div>
      <div class="fan" style="left:224px;top:209px"><i role="img" aria-label="Fan photo"></i>Anil</div>
      <div style="position:absolute;left:8px;bottom:6px;font-size:11px;color:#555;display:flex;align-items:center;gap:5px"><i style="width:12px;height:12px;background:#3b5998;display:inline-block"></i>Social plugin</div>
    </div>
  </aside>

  <div class="abs box promo" style="left:61px;width:359px">
    <div class="promo-fill" role="img" aria-label="Photo of hands exchanging house keys" style="background:linear-gradient(90deg,#111 40%,#6a4a2a)">
      <div style="position:absolute;left:16px;top:18px;color:var(--gold);font-weight:700;font-size:19px">NEW LISTING ADDED DAILY</div>
      <div style="position:absolute;left:16px;top:42px;color:#fff;font-size:16px">Click here to view them now!</div>
    </div>
  </div>
  <div class="abs box promo" style="left:440px;width:359px">
    <div class="promo-fill" role="img" aria-label="Photo of a large two-storey house" style="background:linear-gradient(90deg,#1e8fd8 45%,#9fc6e4 70%,#8b7d6a)">
      <div style="position:absolute;left:12px;top:16px;color:#fff;font-weight:700;font-size:17px;line-height:1.15">FOUND YOUR<br>DREAM HOME</div>
      <div style="position:absolute;left:12px;top:58px;color:#fff;font-size:15px">Click here to qualify!</div>
    </div>
  </div>

  <nav class="abs footer-nav">
    <span>Home</span>|<span>Buyers</span>|<span>Sellers</span>|<span>Agents</span>|<span>Property Management</span>|<span>Field &amp; Inspection Services</span>|<span>Latest News</span>|<span>Blog</span>|<span>Contact</span>
  </nav>
  <footer class="abs footer"></footer>
  <div class="abs office" style="left:59px"><b>Office 1</b>Phone: 555- 478-2037<br>Fax: 555- 253-5736<br>info@harborlinegroup.com</div>
  <div class="abs office" style="left:329px"><b>Office 2</b>Phone: 555- 478-2037<br>Fax: 555- 253-5736<br>info@harborlinegroup.com</div>
  <div class="abs office" style="left:600px"><b>Office 3</b>Phone: 555- 478-2037<br>Fax: 555- 253-5736<br>info@harborlinegroup.com</div>
  <div class="abs" style="left:890px;top:2124px;color:#fff;font-size:14px;font-weight:700">Get In Touch</div>
  <div class="abs social" style="left:889px;background:#5a7ab8"></div>
  <div class="abs social" style="left:935px;background:#2fa9e6"></div>
  <div class="abs social" style="left:981px;background:#f28c1e"></div>
  <div class="abs social" style="left:1028px;background:#e8e8e8"></div>
  <div class="abs" style="left:80px;top:2228px;width:1040px;height:1px;background:rgba(255,255,255,.25)"></div>
  <div class="abs" style="left:0;top:2240px;width:1200px;text-align:center;color:#fff;font-size:13px">&#169; 2013, All Rights Reserved, Harbor Line Realty Group</div>

</div>
</body>
</html>
```